TONVALE - A modern gin bottle label

Design of a bottle label in a modern fresh design. The name of the gin is "TONVALE Phantom Batch K7". Please take a look at the tonvale.de website. on the main page of tonvale.de you can breathe the design direction here: 1) the taste of the gin should be composed of 10 botanicals ... an important scent note. ) a distinctive flavor is spicy and fresh 3.) The filling volume is 0.5 liters 4.) the alcohol content is 43% vol. 5.) the variety is called "dry gin" 6.) tonvale stands for "energy" and "love"

Target Market(s)

Alcohol consumer

Colors

Designer to choose colors to be used in the design.

Requirements
Must have
• the tonvale corporate logo must be included, the name of the gin is "TONVALE Phantom Batch K7"
Nice to have
• Please use the bottles template in the appendix. (The Black Bottles) they can use the saying "DESTILLED & BOTTLED BY OLD MARINER" in small letters

```html
<!DOCTYPE html>
<html lang="en">
<head>
<meta charset="utf-8">
<title>TONVALE Phantom Batch K7 – Dry Gin Label</title>
<link rel="stylesheet" href="https://fonts.googleapis.com/css2?family=Montserrat:wght@600;900&family=Noto+Serif:wght@400;700&display=swap">
<style>
  :root {
    --page: #ffffff;
    --label: #18181c;
    --ink: #ffffff;
    --amber: #f5a01f;
    --tangerine: #f0592a;
    --fruit-orange: #f28a25;
    --leaf-green: #2f6f4e;
  }
  html, body {
    margin: 0;
    width: 776px;
    height: 1200px;
    overflow: hidden;
    background: var(--page);
  }
  .label-art { display: block; width: 776px; height: 1200px; }
  .label-body { fill: var(--label); }
  .brand-name {
    font-family: "Montserrat", sans-serif;
    font-weight: 600;
    font-size: 19px;
    letter-spacing: 3px;
    fill: var(--ink);
  }
  .arc-line {
    font-family: "Noto Serif", serif;
    font-weight: 700;
    font-size: 31px;
    fill: var(--ink);
  }
  .edition-title {
    font-family: "Montserrat", sans-serif;
    font-weight: 900;
    font-size: 124px;
    fill: var(--ink);
  }
  .batch-mark {
    font-family: "Montserrat", sans-serif;
    font-weight: 900;
    font-size: 40px;
    fill: var(--label);
  }
  .variety {
    font-family: "Noto Serif", serif;
    font-weight: 700;
    font-size: 44px;
    letter-spacing: 3px;
    fill: var(--ink);
  }
  .abv-value {
    font-family: "Noto Serif", serif;
    font-weight: 700;
    font-size: 17px;
    fill: var(--ink);
  }
  .abv-unit {
    font-family: "Montserrat", sans-serif;
    font-weight: 600;
    font-size: 10px;
    fill: var(--ink);
  }
  .volume {
    font-family: "Noto Serif", serif;
    font-weight: 400;
    font-size: 29px;
    fill: var(--ink);
  }
</style>
</head>
<body>
<svg class="label-art" viewBox="0 0 776 1200" xmlns="http://www.w3.org/2000/svg">
  <defs>
    <linearGradient id="band-top" x1="0" x2="1" y1="0" y2="0">
      <stop offset="0" stop-color="var(--amber)"/>
      <stop offset="1" stop-color="var(--tangerine)"/>
    </linearGradient>
    <linearGradient id="band-bottom" x1="0" x2="1" y1="0" y2="0">
      <stop offset="0" stop-color="var(--tangerine)"/>
      <stop offset="1" stop-color="var(--amber)"/>
    </linearGradient>
    <linearGradient id="fruit-field" x1="0" x2="0" y1="0" y2="1">
      <stop offset="0" stop-color="var(--fruit-orange)" stop-opacity="0.85"/>
      <stop offset="0.55" stop-color="var(--leaf-green)" stop-opacity="0.55"/>
      <stop offset="1" stop-color="var(--label)" stop-opacity="1"/>
    </linearGradient>
    <path id="arc-top" d="M 222 545 Q 390 420 562 545"/>
    <path id="arc-bottom" d="M 268 925 Q 390 995 512 920"/>
  </defs>

  <!-- label panel -->
  <rect class="label-body" x="61" y="116" width="654" height="967"/>
  <rect class="band" x="61" y="116" width="654" height="14" fill="url(#band-top)"/>
  <rect class="band" x="61" y="1069" width="654" height="14" fill="url(#band-bottom)"/>

  <!-- botanical artwork area -->
  <rect class="botanical-art" x="61" y="130" width="654" height="184" fill="url(#fruit-field)"
        role="img" aria-label="Illustration of orange halves, segments and green leaves along the top edge"/>

  <!-- brand -->
  <text class="brand-name" x="101" y="430">TONVALE</text>

  <!-- distilled & bottled -->
  <text class="arc-line" text-anchor="middle">
    <textPath href="#arc-top" startOffset="50%">distilled &amp; bottled</textPath>
  </text>

  <!-- product name -->
  <text class="edition-title" x="130" y="661" textLength="516" lengthAdjust="spacingAndGlyphs">PHANTOM</text>
  <text class="edition-title" x="120" y="772" textLength="400" lengthAdjust="spacingAndGlyphs">BATCH</text>
  <circle class="batch-disc" cx="600" cy="727" r="48" fill="var(--ink)"/>
  <text class="batch-mark" x="600" y="741" text-anchor="middle">K7</text>

  <!-- variety -->
  <text class="variety" x="388" y="850" text-anchor="middle">DRY GIN</text>

  <!-- by old mariner -->
  <text class="arc-line" text-anchor="middle">
    <textPath href="#arc-bottom" startOffset="50%">by old mariner</textPath>
  </text>

  <!-- abv badge -->
  <g class="abv-badge">
    <circle cx="635" cy="947" r="38" fill="var(--ink)"/>
    <circle cx="635" cy="947" r="33" fill="var(--label)"/>
    <circle cx="635" cy="947" r="30" fill="none" stroke="var(--ink)" stroke-width="1.5"/>
    <text class="abv-value" x="635" y="950" text-anchor="middle">43%</text>
    <text class="abv-unit" x="635" y="964" text-anchor="middle">vol.</text>
  </g>

  <text class="volume" x="636" y="1027" text-anchor="middle">0.5L</text>
</svg>
</body>
</html>
```